New design of old website

We need a new design of our domain name reseller website.

kavirnodo.com

we would also like new design for Logo and all.

the site will be in English and portuguesse,

Domain

```html
<!DOCTYPE html>
<html lang="en">
<head>
<meta charset="utf-8">
<title>kavirnodo — The best solution for your business</title>
<link rel="stylesheet" href="https://fonts.googleapis.com/css2?family=Signika:wght@300;400;600&display=swap">
<style>
  :root {
    --coral: #ef6b6b;
    --yellow: #f7ee2c;
    --white: #ffffff;
    --sand: #ebe4da;
    --tagline: #d8d2c8;
    --body-text: #5a5a5a;
    --font-main: "Signika", "Helvetica Neue", Arial, sans-serif;
  }
  * { margin: 0; padding: 0; box-sizing: border-box; }
  html, body { width: 1200px; height: 1151px; overflow: hidden; background: var(--white); }
  body { font-family: var(--font-main); position: relative; }

  .site-header { position: absolute; left: 0; top: 0; width: 1200px; height: 124px; }
  .brand { position: absolute; left: 146px; top: 27px; display: flex; align-items: center; gap: 10px; }
  .brand-dot { width: 52px; height: 52px; border-radius: 50%; background: var(--coral); }
  .brand-name { font-size: 38px; font-weight: 300; color: var(--coral); letter-spacing: -0.5px; }
  .tagline { position: absolute; left: 489px; top: 38px; font-size: 37px; font-weight: 300; color: var(--tagline); letter-spacing: 0.2px; }

  .hero { position: absolute; left: 0; top: 124px; width: 1200px; height: 410px; }
  .hero-bg { position: absolute; inset: 0; }
  .main-nav { position: absolute; top: 17px; left: 0; width: 1200px; }
  .main-nav a { position: absolute; top: 0; font-size: 19px; font-weight: 300; color: var(--yellow); text-decoration: none; line-height: 28px; }
  .main-nav a.is-active { background: var(--white); color: var(--coral); border-radius: 14px; padding: 0 9px; margin-left: -9px; }
  .hero-photo { position: absolute; left: 240px; top: 52px; width: 310px; height: 300px;
    background: radial-gradient(ellipse at 60% 55%, #d7c84a 0%, #e4a28a 45%, rgba(239,107,107,0) 72%); }
  .hero-title { position: absolute; left: 648px; top: 82px; font-size: 41px; font-weight: 300; color: var(--white); line-height: 49px; }
  .hero-title em { font-style: normal; color: var(--yellow); }
  .hero-cta { position: absolute; left: 645px; top: 239px; width: 257px; height: 44px; border-radius: 13px; background: var(--white);
    color: var(--coral); font-size: 20px; font-weight: 300; line-height: 44px; text-align: center; text-decoration: none; }
  .skyline { position: absolute; left: 785px; top: 292px; width: 305px; height: 110px;
    background: linear-gradient(to top, rgba(255,255,255,0.95) 0%, rgba(255,255,255,0.75) 60%, rgba(255,255,255,0) 100%); }

  .features-slider { position: absolute; left: 0; top: 557px; width: 1200px; }
  .slider-arrow { position: absolute; top: 36px; width: 44px; height: 44px; border-radius: 50%; background: var(--coral); }
  .slider-arrow svg { display: block; }
  .slider-arrow.prev { left: 71px; }
  .slider-arrow.next { left: 1087px; }
  .feature-card { position: absolute; top: 0; width: 292px; }
  .feature-card .card-image { width: 292px; height: 131px; border-radius: 8px; }
  .feature-card h3 { margin-top: 24px; font-size: 21px; font-weight: 300; color: var(--coral); }
  .feature-card p { margin-top: 8px; font-size: 20px; font-weight: 300; color: var(--body-text); line-height: 28px; }

  .benefits { position: absolute; left: 2px; top: 850px; width: 1198px; height: 222px; background: var(--sand); }
  .benefit { position: absolute; top: 28px; width: 172px; height: 172px; border-radius: 50%; background: var(--white); }
  .benefit svg.icon { position: absolute; left: 46px; top: 46px; }
  .benefit-number { position: absolute; left: -8px; top: -6px; width: 52px; height: 62px; }
  .benefit-number span { position: absolute; left: 0; top: 0; width: 52px; height: 52px; line-height: 52px; text-align: center;
    font-size: 28px; font-weight: 600; color: var(--white); }
  .benefit-labels { position: absolute; left: 0; top: 1086px; width: 1200px; }
  .benefit-labels span { position: absolute; font-size: 29px; font-weight: 600; color: var(--coral); white-space: nowrap; transform: translateX(-50%); }
</style>
</head>
<body>

<header class="site-header">
  <div class="brand">
    <span class="brand-dot"></span>
    <span class="brand-name">kavirnodo</span>
  </div>
  <p class="tagline">The best solution for your business</p>
</header>

<section class="hero">
  <svg class="hero-bg" width="1200" height="410" viewBox="0 0 1200 410" aria-hidden="true">
    <path fill="var(--coral)" d="M0 0 H1200 V380 C1080 380 960 370 830 368 C640 360 480 352 330 354 C180 356 70 364 0 380 Z"/>
  </svg>

  <nav class="main-nav">
    <a href="#" style="left:164px">Home</a>
    <a href="#" style="left:248px">Why us</a>
    <a href="#" class="is-active" style="left:342px">Products</a>
    <a href="#" style="left:448px">Services</a>
    <a href="#" style="left:549px">Lifestyle</a>
    <a href="#" style="left:648px">Reseller</a>
    <a href="#" style="left:747px">Contact</a>
    <a href="#" style="left:998px">Login</a>
  </nav>

  <div class="hero-photo" role="img" aria-label="Photo of a smiling woman in a yellow top holding an open laptop"></div>

  <h1 class="hero-title">More than <em>15 years</em><br><em>of experience</em> in the<br>domain name business.</h1>
  <a href="#" class="hero-cta">Get to know our services.</a>

  <div class="skyline" role="img" aria-label="White city skyline silhouette with trees"></div>
</section>

<section class="features-slider">
  <a href="#" class="slider-arrow prev" aria-label="Previous">
    <svg width="44" height="44" viewBox="0 0 44 44"><path d="M27 13 L14 22 L27 31 Z" fill="var(--white)"/></svg>
  </a>

  <article class="feature-card" style="left:134px">
    <div class="card-image" role="img" aria-label="Photo of two women laughing in bright sunlight"
      style="background:linear-gradient(100deg,#bcd9ee 0%,#e6eef2 40%,#e8c9a6 75%,#d9b58c 100%)"></div>
    <h3>Lorium Ipsum</h3>
    <p>Lorem ipsum dolor sit amet, sed<br>do eiusmod tempor incididunt ut</p>
  </article>

  <article class="feature-card" style="left:452px">
    <div class="card-image" role="img" aria-label="Photo of a relaxed man in a suit with his feet up in striped socks"
      style="background:linear-gradient(100deg,#eceeee 0%,#c8cdd2 40%,#8f99a4 65%,#d4b25a 85%,#eceeee 100%)"></div>
    <h3>Lorium Ipsum</h3>
    <p>Lorem ipsum dolor sit amet, sed<br>do eiusmod tempor incididunt ut</p>
  </article>

  <article class="feature-card" style="left:771px">
    <div class="card-image" role="img" aria-label="Photo of a woman in a red jacket among yellow autumn leaves"
      style="background:linear-gradient(100deg,#e6e23a 0%,#c9cf2e 40%,#7a8a2a 62%,#3a3f6e 80%,#c33a2e 100%)"></div>
    <h3>Lorium Ipsum</h3>
    <p>Lorem ipsum dolor sit amet, sed<br>do eiusmod tempor incididunt ut</p>
  </article>

  <a href="#" class="slider-arrow next" aria-label="Next">
    <svg width="44" height="44" viewBox="0 0 44 44"><path d="M17 13 L30 22 L17 31 Z" fill="var(--white)"/></svg>
  </a>
</section>

<section class="benefits">
  <div class="benefit" style="left:184px">
    <div class="benefit-number">
      <svg width="52" height="62" viewBox="0 0 52 62"><circle cx="26" cy="26" r="26" fill="var(--coral)"/><path d="M28 50 L38 62 L40 44 Z" fill="var(--coral)"/></svg>
      <span>1</span>
    </div>
    <svg class="icon" width="80" height="80" viewBox="0 0 80 80" aria-hidden="true">
      <path d="M40 10 L48 14 L56 12 L64 18 V42 C64 56 52 66 40 72 C28 66 16 56 16 42 V18 L24 12 L32 14 Z" fill="var(--coral)"/>
      <path d="M40 20 H58 V40 H40 Z M40 40 H22 V44 C22 52 30 60 40 64 Z" fill="var(--white)"/>
    </svg>
  </div>

  <div class="benefit" style="left:415px">
    <div class="benefit-number">
      <svg width="52" height="62" viewBox="0 0 52 62"><circle cx="26" cy="26" r="26" fill="var(--coral)"/><path d="M28 50 L38 62 L40 44 Z" fill="var(--coral)"/></svg>
      <span>2</span>
    </div>
    <svg class="icon" width="80" height="80" viewBox="0 0 80 80" aria-hidden="true">
      <rect x="6" y="14" width="70" height="52" rx="4" fill="var(--coral)"/>
      <rect x="13" y="21" width="56" height="38" fill="var(--white)"/>
      <circle cx="41" cy="32" r="7" fill="var(--coral)"/>
      <path d="M28 56 C28 46 34 42 41 42 C48 42 54 46 54 56 Z" fill="var(--coral)"/>
      <rect x="36" y="66" width="10" height="6" fill="var(--coral)"/>
      <rect x="24" y="72" width="34" height="4" rx="2" fill="var(--coral)"/>
    </svg>
  </div>

  <div class="benefit" style="left:652px">
    <div class="benefit-number">
      <svg width="52" height="62" viewBox="0 0 52 62"><circle cx="26" cy="26" r="26" fill="var(--coral)"/><path d="M28 50 L38 62 L40 44 Z" fill="var(--coral)"/></svg>
      <span>3</span>
    </div>
    <svg class="icon" width="80" height="80" viewBox="0 0 80 80" aria-hidden="true">
      <g fill="var(--coral)">
        <circle cx="28" cy="52" r="17"/>
        <g transform="translate(28 52)">
          <rect x="-5" y="-24" width="10" height="48" rx="2"/>
          <rect x="-5" y="-24" width="10" height="48" rx="2" transform="rotate(45)"/>
          <rect x="-5" y="-24" width="10" height="48" rx="2" transform="rotate(90)"/>
          <rect x="-5" y="-24" width="10" height="48" rx="2" transform="rotate(135)"/>
        </g>
        <circle cx="56" cy="24" r="13"/>
        <g transform="translate(56 24)">
          <rect x="-4" y="-19" width="8" height="38" rx="2"/>
          <rect x="-4" y="-19" width="8" height="38" rx="2" transform="rotate(45)"/>
          <rect x="-4" y="-19" width="8" height="38" rx="2" transform="rotate(90)"/>
          <rect x="-4" y="-19" width="8" height="38" rx="2" transform="rotate(135)"/>
        </g>
      </g>
      <circle cx="28" cy="52" r="10" fill="var(--white)"/>
      <circle cx="28" cy="52" r="5" fill="var(--coral)"/>
      <circle cx="56" cy="24" r="7" fill="var(--white)"/>
      <circle cx="56" cy="24" r="3" fill="var(--coral)"/>
    </svg>
  </div>

  <div class="benefit" style="left:882px">
    <div class="benefit-number">
      <svg width="52" height="62" viewBox="0 0 52 62"><circle cx="26" cy="26" r="26" fill="var(--coral)"/><path d="M28 50 L38 62 L40 44 Z" fill="var(--coral)"/></svg>
      <span>4</span>
    </div>
    <svg class="icon" width="80" height="80" viewBox="0 0 80 80" aria-hidden="true">
      <path d="M2 40 C14 24 26 17 40 17 C54 17 66 24 78 40 C66 56 54 63 40 63 C26 63 14 56 2 40 Z" fill="var(--coral)"/>
      <path d="M10 40 C20 28 30 23 40 23 C50 23 60 28 70 40 C60 52 50 57 40 57 C30 57 20 52 10 40 Z" fill="var(--white)"/>
      <circle cx="40" cy="40" r="15" fill="var(--coral)"/>
      <circle cx="40" cy="40" r="9" fill="var(--white)"/>
      <circle cx="40" cy="40" r="5" fill="var(--coral)"/>
    </svg>
  </div>
</section>

<div class="benefit-labels">
  <span style="left:270px">Security</span>
  <span style="left:524px">TLD Expecilist</span>
  <span style="left:776px">Automation</span>
  <span style="left:1025px">Service</span>
</div>

</body>
</html>
```